Home Health Care Agency Needs a Website (Seeking a PSD)

We need a user friendly website for a Home Health Care Agency. Our service is for the elderly and disabled. Frequently the busy professional middle-aged married daughter will use the website to arrange in-home care for an aging parent. Therefore, our website is primarily geared towards middle-aged women. In-home care is typically 24 hours a day so, a feeling of trustworthiness and security should be effectively conveyed. (Seeking a PSD- however, if you also offer coding, please let us know the cost.)

Target Market(s)

Frequently the busy professional middle-aged married daughter (possibly out of state) will use the website to arrange in-home care for an aging parent.

Industry/Entity Type

Security

Requirements
Must have
• Website must be clean, uncluttered and professional. The following menu pages are requested: Home, About Us, Services, Resources, FAQ, Employment & Contact.
Should not have
• Must not be too whimsical.

```html
<!DOCTYPE html>
<html lang="en">
<head>
<meta charset="utf-8">
<title>Harbor Home Health</title>
<link rel="stylesheet" href="https://fonts.googleapis.com/css2?family=Open+Sans:wght@400;600;700&family=Ubuntu:wght@300;400;500;700&display=swap">
<style>
:root{
  --sky:#4fc3ea;
  --sky-deep:#1a8fcc;
  --royal:#1668b4;
  --slate:#3e4c58;
  --slate-dark:#4b5a66;
  --ink:#2b2b2b;
  --red:#d42a22;
  --gold:#f7c20f;
  --panel:#e8e6e2;
  --card:#e6e4e0;
  --paper:#f4f7f9;
  --band:#e2eff7;
}
*{margin:0;padding:0;box-sizing:border-box}
html,body{width:1117px;height:1200px;overflow:hidden}
body{position:relative;background:var(--paper);font-family:"Ubuntu",sans-serif;color:var(--ink)}
.abs{position:absolute}

/* header */
.brand{left:141px;top:38px;display:flex;align-items:center;gap:10px}
.brand-mark{width:26px;height:26px;border-radius:50%;background:var(--sky)}
.brand-name{font:700 30px/1 "Ubuntu",sans-serif;color:var(--sky)}
.social{top:6px;width:28px;height:28px;border-radius:50%;background:#7e8a94;border:2px solid #c3cad0}
.callbar{left:552px;top:79px;width:424px;height:30px;background:var(--slate-dark);display:flex;align-items:center;padding-left:10px;font-family:"Ubuntu",sans-serif;color:#fff}
.callbar .lbl{color:var(--gold);font-weight:500;font-size:17px;margin-right:8px}
.callbar .num{font-weight:500;font-size:19px;margin-right:10px}
.callbar .or{background:#fff;color:var(--red);font-weight:700;font-size:16px;border-radius:50%;padding:4px 11px;margin-right:10px}
.callbar .mail{font-size:12px}

.nav{left:0;top:118px;width:1117px;height:30px;background:var(--sky);border-bottom:1px solid #2c8cb8}
.nav a{position:absolute;top:8px;color:#fff;font:400 12.5px/1 "Ubuntu",sans-serif;text-decoration:none;letter-spacing:.2px}

.hero-band{left:0;top:148px;width:1117px;height:348px;background:var(--band)}
.hero{left:141px;top:150px;width:835px;height:345px;background:linear-gradient(90deg,#b9a9a4 0%,#cfc4c0 35%,#ebe9e8 60%,#f2f1f0 100%);border:1px solid #7d8b95}

.content-band{left:0;top:496px;width:1117px;height:40px;background:linear-gradient(#d8ecf6,var(--paper))}

/* welcome */
.welcome{left:156px;top:520px;font:700 26px/1 "Open Sans",sans-serif;color:var(--sky-deep);letter-spacing:.5px}
.intro{left:156px;top:565px;width:540px;font:400 10.6px/16.4px "Open Sans",sans-serif;color:#333;letter-spacing:.3px}
.more{left:616px;top:654px;font:600 11px/1 "Open Sans",sans-serif;color:var(--red)}

/* service cards */
.card{top:694px;width:174px;height:259px;background:var(--card)}
.card h2{height:29px;background:var(--sky);color:#fff;font:700 18px/29px "Open Sans",sans-serif;text-align:center;letter-spacing:.4px}
.card .photo{height:132px}
.card p{margin:7px 8px 0;text-align:center;font:400 11.4px/13.3px "Ubuntu",sans-serif;color:#222}
.card .btn{position:absolute;left:41px;top:230px;width:91px;height:20px;background:var(--sky);color:#fff;text-align:center;font:400 11px/20px "Ubuntu",sans-serif}

/* side panel */
.side{left:731px;top:520px;width:245px;height:433px;background:var(--panel);border-radius:3px}
.qc{left:748px;top:537px;width:212px;height:248px;background:#fff}
.qc-head{left:748px;top:537px;width:212px;height:29px;background:var(--sky);color:#fff;font:700 15px/29px "Ubuntu",sans-serif;padding-left:56px}
.qc-icon{left:766px;top:529px;width:30px;height:36px;background:#fff;border:1px solid #c9d3da;transform:rotate(-6deg)}
.field{left:764px;width:177px;height:23px;background:#f3f3f3;border:1px solid #cfcfcf;font:400 10px/21px "Open Sans",sans-serif;color:#9a9a9a;padding-left:8px;letter-spacing:.3px}
.field svg{position:absolute;right:6px;top:5px}
.field.msg{height:66px;line-height:1;padding-top:8px}
.send{left:764px;top:744px;width:177px;height:29px;background:var(--royal);color:#fff;text-align:center;font:500 15px/29px "Ubuntu",sans-serif}
.promo{left:747px;top:805px;width:214px;height:126px;background:#f8f8f8;border:1px solid #b7b7b7;text-align:center;padding-top:10px;font:700 20px/22px "Ubuntu",sans-serif;color:#111}
.promo em{font-style:normal;color:var(--red)}

/* footer */
.footer{left:0;top:984px;width:1117px;height:187px;background:var(--slate)}
.foot-h{top:996px;font:300 18px/1 "Ubuntu",sans-serif;color:#dfe4e8;letter-spacing:.3px}
.foot-list{top:1025px;list-style:none;font:400 12px/19.6px "Ubuntu",sans-serif;color:#fff}
.divider{left:339px;top:1010px;width:1px;height:143px;background:#1f262c}
.contact-line{left:789px;font:400 11.5px/14.5px "Ubuntu",sans-serif;color:#fff;display:flex;gap:6px;align-items:flex-start}
.bottom{left:0;top:1171px;width:1117px;height:29px;background:var(--slate-dark);color:#d6dce1;text-align:center;font:400 10.5px/29px "Ubuntu",sans-serif;letter-spacing:.3px}
</style>
</head>
<body>

<header>
  <div class="abs brand"><span class="brand-mark"></span><span class="brand-name">Harbor Home Health</span></div>
  <span class="abs social" style="left:872px" aria-label="Social link"></span>
  <span class="abs social" style="left:909px" aria-label="Social link"></span>
  <span class="abs social" style="left:947px" aria-label="Social link"></span>
  <div class="abs callbar">
    <span class="lbl">Call -</span><span class="num">(555) 014 2290</span><span class="or">Or</span><span class="lbl">Mail -</span><span class="mail">info@hhhcare.com</span>
  </div>
  <nav class="abs nav">
    <a style="left:159px">HOME</a><a style="left:231px">ABOUT US</a><a style="left:331px">SERVICES</a><a style="left:425px">RESOURCES</a><a style="left:533px">FAQ</a><a style="left:598px">EMPLOYMENT</a><a style="left:718px">CONTACT US</a>
  </nav>
</header>

<div class="abs hero-band"></div>
<div class="abs hero" role="img" aria-label="Photo of a smiling nurse helping an elderly woman at home"></div>
<div class="abs content-band"></div>

<main>
  <h1 class="abs welcome">WELCOME TO HARBOR HOME HEALTH</h1>
  <p class="abs intro">Lorem Ipsum. Proin gravida nibh vel velit auctor aliquet. Aenean sollicitudin, lorem quis bibendum auctor, nisi elit consequat ipsum, nec sagittis sem nibh id elit. Duis sed odio sit am nibh vulputate cursus a sit amet mauris. Morbi accumsan ipsum velit. Nam nec tellus a odio tincidunt auctor a ornare odio. Sed non&nbsp; mauris vitae erat consequat auctor eu in elit. Class in aptent taciti sociosq ad litora torquent per conubia nostra, per inceptos himenaeos. Mauris i erat justo. Nullam ac urna</p>
  <span class="abs more">Learn more ›</span>

  <section class="abs card" style="left:156px">
    <h2>COMPANIONSHIP</h2>
    <div class="photo" role="img" aria-label="Photo of two women sharing tea and laughing" style="background:linear-gradient(#a8b98a,#c9a47a 70%,#d9b27a)"></div>
    <p>Lorem Ipsum. Proin gravida nibh vel velit auctor aliquet Aenean sollicitudin, lorem quis bibendum auctor</p>
    <span class="btn">Learn more</span>
  </section>
  <section class="abs card" style="left:339px">
    <h2>ASSISTED LIVING</h2>
    <div class="photo" role="img" aria-label="Photo of a carer with an elderly woman in a wheelchair" style="background:linear-gradient(90deg,#ece9e6,#d8cfc8 60%,#c9a9a8)"></div>
    <p>Lorem Ipsum. Proin gravida nibh vel velit auctor aliquet Aenean sollicitudin, lorem quis bibendum auctor</p>
    <span class="btn">Learn more</span>
  </section>
  <section class="abs card" style="left:522px">
    <h2>NURSING</h2>
    <div class="photo" role="img" aria-label="Photo of a nurse in scrubs caring for a seated elderly woman" style="background:linear-gradient(90deg,#5e5a63,#9a7f98 45%,#6f9a9a)"></div>
    <p>Lorem Ipsum. Proin gravida nibh vel velit auctor aliquet Aenean sollicitudin, lorem quis bibendum auctor</p>
    <span class="btn">Learn more</span>
  </section>
</main>

<aside>
  <div class="abs side"></div>
  <div class="abs qc"></div>
  <div class="abs qc-head">Quick Contact</div>
  <div class="abs qc-icon"></div>
  <div class="abs field" style="top:578px">Enter your name
    <svg width="12" height="12" viewBox="0 0 12 12"><circle cx="6" cy="3.5" r="3" fill="#aaa"/><path d="M0 12a6 5 0 0 1 12 0z" fill="#aaa"/></svg></div>
  <div class="abs field" style="top:609px">Enter your email
    <svg width="13" height="11" viewBox="0 0 13 11"><rect x=".5" y=".5" width="12" height="10" fill="none" stroke="#aaa"/><path d="M.5 .5 6.5 6l6-5.5" fill="none" stroke="#aaa"/></svg></div>
  <div class="abs field" style="top:640px">Enter your phone
    <svg width="13" height="11" viewBox="0 0 13 11"><path d="M0 3q6.5-4 13 0v2h-3V3.5h-7V5H0z" fill="#aaa"/><rect x="2" y="6" width="9" height="5" rx="1" fill="#aaa"/></svg></div>
  <div class="abs field msg" style="top:671px">Message</div>
  <div class="abs send">Send</div>
  <div class="abs promo">Get <em>CLEAR</em>,<br><em>CORRECT</em> &amp;<br><em>CREDIBLE</em> answers<br>to your&nbsp; questions<br>here.</div>
</aside>

<footer>
  <div class="abs footer"></div>
  <h3 class="abs foot-h" style="left:157px">Quick link</h3>
  <ul class="abs foot-list" style="left:157px"><li>Home</li><li>About Us</li><li>Services</li><li>Resources</li><li>FAQ</li><li>Employment</li><li>Contact Us</li></ul>
  <div class="abs divider"></div>
  <h3 class="abs foot-h" style="left:451px">Terms &amp; Privacy</h3>
  <ul class="abs foot-list" style="left:452px"><li>Terms of Use</li><li>Privacy Policy</li><li>Collection of Information</li></ul>
  <h3 class="abs foot-h" style="left:789px">Contact info</h3>
  <div class="abs contact-line" style="top:1026px">
    <svg width="12" height="18" viewBox="0 0 12 18"><path d="M6 1a5 5 0 0 0-5 5c0 4 5 11 5 11s5-7 5-11a5 5 0 0 0-5-5z" fill="none" stroke="#aab3ba" stroke-width="1.5"/><circle cx="6" cy="6" r="2" fill="#aab3ba"/></svg>
    <span>Lorem Ipsum. met mauris.<br>Morbi accumsan ipsum velit.</span></div>
  <div class="abs contact-line" style="top:1069px">
    <svg width="13" height="11" viewBox="0 0 13 11"><path d="M0 3q6.5-4 13 0v2h-3V3.5h-7V5H0z" fill="#aab3ba"/><rect x="2" y="6" width="9" height="5" rx="1" fill="#aab3ba"/></svg>
    <span style="font-size:12px">(555) 014 2290</span></div>
  <div class="abs contact-line" style="top:1099px">
    <svg width="13" height="11" viewBox="0 0 13 11"><rect x=".5" y=".5" width="12" height="10" fill="none" stroke="#aab3ba"/><path d="M.5 .5 6.5 6l6-5.5" fill="none" stroke="#aab3ba"/></svg>
    <span style="font-size:12px">info@hhhcare.com</span></div>
  <div class="abs bottom">© 2013 HARBOR HOME HEALTH, All rights reserved</div>
</footer>

</body>
</html>
```